Business Card Design for digital storytelling business

I need a business card for a workshop/consulting/coaching business.

Company Name: The Bright Harbor

Tagline: Simple Tools for Your Family's Stories

What we do: Through workshops, webinars, and coaching we teach you how to capture, tell and share your important memories and stories using readily available digital tools. We will help you tell your life story in a format to share with your family now and in the future.
Updates

I just received a toll free number that I would like included on the designs. If the addition of a phone number would significantly alter your design, please submit an altered version. The number is 877-512-6098

Target Market(s)

Adults in US between ages of 35-70 interested in capturing, preserving and sharing memories and life stories in a digital format.
Could include the following:

-People touched by illness or tragedy who need to tell their own or a loved one's life story
-Grandparents wanting to share stories and wisdom with grandchildren living far away
-People with aging parents who want to capture their stories in a format to pass on to their children
-Alzheimer's patients and their families
-People wanting to transfer analog photos to digital; or wanting to organize digital photos into something that tells a story

Industry/Entity Type

Digital

Requirements
Must have
• Must include business name, logo, tagline

Contact information (see file)
Social media information

Fonts easily readable by aging eyes. Good contrast.

Nice to have
• Color preferences: blue, green, yellow/gold
Blue denotes the calm, non-pressured way that I teach. It is for the healing that comes from telling your story. It represents time and space that are bridged in the digital environment.
Green is for growth, the future, the family tree, Vines that grow and branch and connect the generations and our hearts.
Yellow/gold is for the legacy of wisdom in our lives and stories. It is for the light of truth we bring to the world by sharing our stories.
Should not have
• No old-style, script fonts.
No Times New Roman

```html
<!DOCTYPE html>
<html lang="en">
<head>
<meta charset="utf-8">
<title>The Bright Harbor – Business Card</title>
<link rel="stylesheet" href="https://fonts.googleapis.com/css2?family=Fira+Sans:wght@400;600&family=Marcellus+SC&display=swap">
<style>
  :root {
    --bg: #1f1f21;
    --paper: #ffffff;
    --navy: #1e4a78;
    --navy-dark: #1a3f68;
    --green: #23a04a;
    --green-text: #1f9a4a;
    --gold: #d9ab3c;
    --gold-text: #d79b2a;
    --ink: #1d3b6b;
    --dot-sky: #3aa9dd;
    --dot-violet: #6b5aa8;
    --dot-lime: #8ab83a;
    --dot-red: #d23a3a;
    --dot-blue: #2f5fa8;
    --dot-yellow: #e7c23a;
  }
  * { margin: 0; padding: 0; box-sizing: border-box; }
  html, body { width: 1200px; height: 800px; overflow: hidden; background: var(--bg); }
  .canvas { position: relative; width: 1200px; height: 800px; }

  .card {
    position: absolute; width: 520px; height: 300px;
    background: var(--paper); overflow: hidden;
    box-shadow: 0 10px 30px rgba(0,0,0,.45);
    font-family: "Fira Sans", sans-serif;
  }

  /* Front */
  .card-front { left: 340px; top: 70px; }
  .front-panel {
    position: absolute; left: 0; right: 0; top: 14px; bottom: 22px;
    background: var(--navy);
  }
  .front-brand {
    position: absolute; left: 0; right: 0; top: 100px;
    display: flex; align-items: center; justify-content: center; gap: 14px;
    color: var(--paper);
  }
  .brand-mark { width: 14px; height: 14px; border-radius: 50%; background: currentColor; flex: none; }
  .brand-name { font-size: 34px; font-weight: 400; line-height: 1; letter-spacing: .3px; white-space: nowrap; }
  .brand-tagline {
    font-family: "Marcellus SC", serif; font-size: 11px; letter-spacing: .6px;
    margin-top: 4px; white-space: nowrap;
  }

  /* Back */
  .card-back { left: 340px; top: 420px; }
  .contact-list {
    position: absolute; right: 14px; top: 14px; list-style: none;
    text-align: right; color: var(--green-text); font-size: 12.5px;
  }
  .contact-list li { display: flex; align-items: center; justify-content: flex-end; gap: 10px; height: 22px; white-space: nowrap; }
  .contact-dot { width: 11px; height: 11px; border-radius: 50%; flex: none; }
  .dot-sky { background: var(--dot-sky); }
  .dot-violet { background: var(--dot-violet); }
  .dot-lime { background: var(--dot-lime); }
  .dot-red { background: var(--dot-red); }
  .dot-blue { background: var(--dot-blue); }
  .dot-yellow { background: var(--dot-yellow); }

  .person { position: absolute; left: 56px; top: 138px; }
  .person-name { color: var(--ink); font-weight: 600; font-size: 17px; }
  .person-role { color: var(--gold-text); font-size: 13px; }

  .green-band {
    position: absolute; left: 0; top: 180px; width: 262px; height: 58px;
    background: var(--green); color: var(--paper);
    display: flex; align-items: center; gap: 10px; padding-left: 18px;
  }
  .green-band .brand-name { font-size: 21px; }
  .green-band .brand-tagline { font-size: 7px; letter-spacing: .3px; margin-top: 2px; }
  .green-band .brand-mark { width: 10px; height: 10px; }

  .blue-strip { position: absolute; left: 0; bottom: 0; width: 300px; height: 36px; background: var(--navy-dark); }
  .blue-block { position: absolute; left: 212px; bottom: 0; width: 90px; height: 56px; background: var(--navy); }
  .gold-panel {
    position: absolute; right: 0; bottom: 0; width: 232px; height: 110px;
    background: var(--gold); border-top-left-radius: 26px;
    display: flex; align-items: center; justify-content: center;
  }
  .gold-panel .brand-mark { width: 40px; height: 40px; background: none; border: 3px solid var(--paper); }
</style>
</head>
<body>
<main class="canvas">
  <section class="card card-front" aria-label="Card front">
    <div class="front-panel"></div>
    <div class="front-brand">
      <span class="brand-mark"></span>
      <div>
        <div class="brand-name">The Bright Harbor</div>
        <div class="brand-tagline">Simple Tools for Your Family's Stories</div>
      </div>
    </div>
  </section>

  <section class="card card-back" aria-label="Card back">
    <ul class="contact-list">
      <li>@BrightHarborCo <span class="contact-dot dot-sky"></span></li>
      <li>www.brightharborstories.com <span class="contact-dot dot-violet"></span></li>
      <li>marian@brightharborstories.com <span class="contact-dot dot-lime"></span></li>
      <li>www.pinspace.net/brightharbor <span class="contact-dot dot-red"></span></li>
      <li>www.friendwall.net/brightharbor <span class="contact-dot dot-blue"></span></li>
      <li>PO Box 218 Maple Cove, RI 02899 <span class="contact-dot dot-yellow"></span></li>
    </ul>
    <div class="person">
      <div class="person-name">Marian Ellsworth</div>
      <div class="person-role">Founder</div>
    </div>
    <div class="blue-block"></div>
    <div class="blue-strip"></div>
    <div class="green-band">
      <span class="brand-mark"></span>
      <div>
        <div class="brand-name">The Bright Harbor</div>
        <div class="brand-tagline">Simple Tools for Your Family's Stories</div>
      </div>
    </div>
    <div class="gold-panel"><span class="brand-mark"></span></div>
  </section>
</main>
</body>
</html>
```